Flyer for a Unique Type of Tax Services

Please refer to the attached sample design for reference. Feel free to change the wording as needed. Here is the project brief:

Objective:
Objective of this flyer is to introduce our services which we are launching soon, which is new of a kind, to our potential customers i.e. online tax return preparation. By looking at the flyer we want our target audience to get convinced of our services and visit our website and register with us. They don’t have to pay anything to register.

Our Competitors:
Currently there are three main options available to get tax returns prepared. First is to buy tax software and get tax return prepared at own, this is the cheapest option. There are studies that suggest that people who are not well aware of tax laws there are chances they miss certain tax refunds by filing returns at their own and potentially lose money. Second option is to go to the local offices of nation-wide tax service companies like Pell & Varne and Morrow Tandy. They open offices only during tax season i.e. Jan through April but they are not available other part of the year and their association with the customers is temporary. Third option is to go to a CPA office which are the most expensive and very few people go for this option.

Weaknesses of the Current Options:
By self-preparing tax returns, there are chances that one can overlook certain tax laws that can provide additional tax credits and exemptions to people and overall they could have got a higher tax refund from the Govt. but they may miss it.
By going to other competitors during the peak time when tax returns are due, there are high chances that they don't have enough time to do research to ensure maximum refunds based on the exact circumstances of the individuals at the peak time as many people come to them during that time. Also they are not available after the tax season to provide them any answers to their questions or provide them tax planning tips to help them save tax in the next season.
By going to the CPA office, they charge a lot of fees and also for any tax advice later during the year, they will charge additional fees.

What we are offering:
We are offering a new option i.e. online tax return preparation through experts. We'll charge the fees competitive to what people are paying to local tax providers. But we will be different than our competitors as we'll be providing value added service if they got their returns prepared through us. Value added services we will be free of any additional cost for our customers who'll get tax return prepared through us.

Our Target Audience:
Our target audience is any person or couple who go to the tax service providers like Pell & Varne or Morrow Tandy to get their tax returns prepared.

How We are Different:
Here is the summary of the unique aspects of our business as compared to the competitors:
- Customers just pay us the price for preparing the annual return and price is comparable and competitive to what they have been paying to other providers.
- Unlike our competitors, we do extensive research to review the circumstances of our customers and explore applicable tax laws to make sure all available tax credits, exemptions, and deductions are taken for our customers, whereas our customers don't usually do such kind of research as during the peak tax season when customers approach them they usually don’t have time to do that kind of research. We start our association with our customers much sooner than the actual due date and this provides us time to do extensive research and we try our best that our customers could get higher tax returns.
- By just getting tax returns prepared through us, we enter into a long-term association with our customers and provide them complimentary tax planning tips throughout the year to help them save tax in the following year
- We are available to our customers year-round to provide complementary answers to any tax related questions without any additional cost e.g. how to save tax when buying a car, whether to buy or lease the care to save tax, for the sole-proprietor business how to save tax by using portion of the home as home-office, how to save tax by using personal car for personal business.
- We also provide answers to other basic financial advise related matters e.g. which insurance product is better, whether full insurance or term-life insurance to chose, how to save for the retirement etc.

Other Details:
Our logo has already been designed and we want the same logo to be used in the flyer. Our website address is: www.FiledRightPlus.com (it is still under construction but to get perspective of what we are trying to offer, visit this alternate website that it not final yet but will give an idea: http://www.filedrightplus.com/wordpress. Fyi, a video at this link is only a placeholder and not relevant to our services)

Requirements
Must have
• Please refer to the sample flyer attached. Feel free to change the design and language.
Should not have
• Please do not put any testimonial on the flyer as reflected in the under construction website.

```html
<!DOCTYPE html>
<html lang="en">
<head>
<meta charset="utf-8">
<title>FiledRight Plus – Tax Services Flyer</title>
<link rel="stylesheet" href="https://fonts.googleapis.com/css2?family=Fira+Sans:ital,wght@0,400;0,600;0,700;1,700&display=swap">
<style>
  :root {
    --brand-blue: #4357a1;
    --band-blue: #3f51a0;
    --accent-orange: #f08a1c;
    --text-white: #ffffff;
    --text-dark: #2a2a2a;
    --footer-light: #ffffff;
    --footer-grey: #dcdcdc;
    --tagline-blue: #3a4fa0;
    --logo-red: #d9442b;
  }
  * { margin: 0; padding: 0; box-sizing: border-box; }
  html, body { width: 780px; height: 1200px; overflow: hidden; background: #ffffff; }
  body { font-family: "Fira Sans", Arial, sans-serif; }

  .flyer { position: relative; width: 780px; height: 1200px; overflow: hidden; background: var(--brand-blue); }

  .questions { position: absolute; left: 12px; top: 38px; width: 736px; list-style: none; }
  .question {
    position: relative; padding-left: 32px; color: var(--text-white);
    font-size: 21px; line-height: 28px; margin-bottom: 26px;
  }
  .question strong { font-weight: 700; }
  .question-icon { position: absolute; left: 0; top: 7px; width: 24px; height: 14px; }

  .offer {
    position: absolute; left: 55px; top: 320px; width: 670px;
    text-align: center; color: var(--text-white); font-size: 21px; line-height: 29px;
  }
  .offer em { color: var(--accent-orange); font-style: italic; font-weight: 700; }

  .desk-photo { position: absolute; left: 0; top: 440px; width: 780px; height: 481px; display: block; }

  .register-band {
    position: absolute; left: 0; top: 921px; width: 780px; height: 43px;
    background: var(--band-blue); display: flex; align-items: center; justify-content: center;
    font-size: 21px; font-weight: 600;
  }
  .register-label { color: var(--text-dark); margin-right: 10px; }
  .register-url { color: var(--text-white); font-weight: 700; }
  .register-url span { color: var(--accent-orange); }

  .footer {
    position: absolute; left: 0; top: 964px; width: 780px; height: 236px;
    background: linear-gradient(to bottom, var(--footer-light) 0%, var(--footer-grey) 100%);
  }
  .brand {
    position: absolute; left: 0; top: 50px; width: 780px;
    display: flex; align-items: center; justify-content: center; gap: 12px;
  }
  .brand-mark { width: 22px; height: 22px; border-radius: 50%; background: var(--logo-red); }
  .brand-name { font-size: 40px; font-weight: 700; color: var(--tagline-blue); letter-spacing: 1px; }

  .tagline {
    position: absolute; left: 18px; top: 132px; width: 744px; text-align: center;
    color: var(--tagline-blue); font-size: 18.5px; font-weight: 700; line-height: 28px;
  }
</style>
</head>
<body>
<main class="flyer">
  <ul class="questions">
    <li class="question">
      <svg class="question-icon" viewBox="0 0 24 14" aria-hidden="true"><path d="M0 5h14V1l10 6-10 6V9H0z" fill="#f08a1c"/></svg>
      Does your Tax Return Preparer have time to do extensive research for you to get <strong>MAXIMUM REFUNDS?</strong>
    </li>
    <li class="question">
      <svg class="question-icon" viewBox="0 0 24 14" aria-hidden="true"><path d="M0 5h14V1l10 6-10 6V9H0z" fill="#f08a1c"/></svg>
      Do you get <strong>Year-Round Free Advice</strong> regarding your Tax Related Questions from your existing Tax Service Provider?
    </li>
    <li class="question">
      <svg class="question-icon" viewBox="0 0 24 14" aria-hidden="true"><path d="M0 5h14V1l10 6-10 6V9H0z" fill="#f08a1c"/></svg>
      Does your existing Tax Service Provider give you <strong>Complimentary Tax Planning Tips</strong> throughout the year to help you save tax in the following financial year?
    </li>
  </ul>

  <p class="offer"><em>If not,</em> then try us, as we provide all these services year-round to our customers who get tax returns prepared through us at no additional COST.</p>

  <svg class="desk-photo" viewBox="0 0 780 481" role="img" aria-label="Photo of hands working a calculator and writing on tax forms at a desk">
    <defs>
      <linearGradient id="deskTones" x1="0.2" y1="0" x2="0.8" y2="1">
        <stop offset="0" stop-color="#f4f4f6"/>
        <stop offset="0.35" stop-color="#e2e2e6"/>
        <stop offset="0.7" stop-color="#c9c7c6"/>
        <stop offset="1" stop-color="#8e8c8e"/>
      </linearGradient>
      <radialGradient id="deskShade" cx="0.25" cy="0.85" r="0.45">
        <stop offset="0" stop-color="#3a3a3e" stop-opacity="0.45"/>
        <stop offset="1" stop-color="#3a3a3e" stop-opacity="0"/>
      </radialGradient>
    </defs>
    <path d="M0 232 C150 120 330 12 510 12 C620 14 700 120 780 470 L780 481 L0 481 Z" fill="url(#deskTones)"/>
    <path d="M0 232 C150 120 330 12 510 12 C620 14 700 120 780 470 L780 481 L0 481 Z" fill="url(#deskShade)"/>
  </svg>

  <div class="register-band">
    <span class="register-label">Register now free at:</span>
    <span class="register-url">www.<span>FiledRight</span>Plus.com</span>
  </div>

  <footer class="footer">
    <div class="brand">
      <span class="brand-mark" aria-hidden="true"></span>
      <span class="brand-name">FiledRight Plus</span>
    </div>
    <p class="tagline">And right away we'll start doing research for you, be available year-round to answer your tax related queries, keep providing you tax planning tips and also guide you on other financial planning matters.</p>
  </footer>
</main>
</body>
</html>
```